We need a design for business cards for our new company. We are a resident safety and security company company that focuses on senior living communities. we provide Nurse call, Access control, CCTV, Wired and wireless network infrastructure, Wander Management, and much more!

Our logo is the circuit board shield. Representing our high tech security solutions. I would like the business card to bring the same theme with perhaps some circuit board traces around the card similar to our logo

```html
<!DOCTYPE html>
<html lang="en">
<head>
<meta charset="utf-8">
<title>ElderNova Business Cards</title>
<link href="https://fonts.googleapis.com/css2?family=Cinzel:wght@500&family=Tinos&display=swap" rel="stylesheet">
<style>
  :root {
    --bg: #2a2a2c;
    --card-white: #ffffff;
    --brand-blue: #2d56b0;
    --blue-light: #3fa4e0;
    --blue-mid: #2f7fd0;
    --blue-deep: #2356a8;
    --blue-navy: #1f4a98;
    --ink: #1d1d1f;
    --rule: #3f66be;
  }
  * { box-sizing: border-box; margin: 0; padding: 0; }
  html, body { width: 1200px; height: 875px; overflow: hidden; }
  body { background: var(--bg); position: relative; font-family: "Tinos", "Times New Roman", serif; }

  .card {
    position: absolute;
    width: 520px;
    height: 298px;
    border-radius: 16px;
    overflow: hidden;
    box-shadow: 0 18px 40px rgba(0,0,0,0.45);
  }

  /* Front */
  .card-front { left: 70px; top: 120px; }
  .front-pattern {
    position: absolute; inset: 0;
    background:
      radial-gradient(ellipse at 85% 15%, rgba(31,74,152,0.55) 0%, rgba(31,74,152,0) 55%),
      radial-gradient(ellipse at 60% 85%, rgba(31,74,152,0.45) 0%, rgba(31,74,152,0) 60%),
      radial-gradient(ellipse at 10% 60%, rgba(120,190,240,0.35) 0%, rgba(120,190,240,0) 50%),
      linear-gradient(160deg, var(--blue-light) 0%, var(--blue-mid) 45%, var(--blue-deep) 100%);
  }
  .front-brand {
    position: absolute; left: 0; right: 0; top: 124px;
    display: flex; justify-content: center; align-items: center; gap: 10px;
    color: var(--card-white);
  }
  .brand-dot { width: 14px; height: 14px; border-radius: 50%; background: var(--card-white); flex: none; }
  .brand-name {
    font-family: "Cinzel", serif; font-weight: 500; letter-spacing: 1px; line-height: 1;
  }
  .front-brand .brand-name { font-size: 36px; }
  .brand-suffix { font-family: "Cinzel", serif; font-size: 9px; line-height: 1; }
  .front-brand .brand-suffix { align-self: flex-end; margin: 0 0 4px -4px; }

  /* Back */
  .card-back { left: 610px; top: 440px; background: var(--card-white); }
  .back-brand {
    position: absolute; left: 40px; top: 56px;
    display: flex; align-items: flex-start; gap: 4px;
    color: var(--brand-blue);
  }
  .back-brand .brand-name { font-size: 54px; }
  .back-brand .brand-suffix { margin-top: 4px; font-size: 10px; }

  .holder {
    position: absolute; left: 108px; top: 176px; width: 180px; text-align: right;
  }
  .holder-name { color: var(--brand-blue); font-size: 24px; line-height: 1.1; white-space: nowrap; }
  .holder-title { color: var(--ink); font-size: 14px; }

  .divider {
    position: absolute; left: 302px; top: 150px;
    width: 1.5px; height: 88px; background: var(--rule);
  }
  .contacts { position: absolute; left: 316px; top: 152px; list-style: none; }
  .contacts li {
    display: flex; align-items: center; gap: 8px;
    font-size: 14px; color: var(--ink); height: 21px; white-space: nowrap;
  }
  .contacts svg { width: 12px; height: 12px; fill: var(--brand-blue); flex: none; }
</style>
</head>
<body>

  <section class="card card-front" aria-label="Business card front">
    <div class="front-pattern" role="img" aria-label="Repeating circuit-trace pattern in light and deep blue tones"></div>
    <div class="front-brand">
      <span class="brand-dot"></span>
      <span class="brand-name">ElderNova</span>
      <span class="brand-suffix">LLC</span>
    </div>
  </section>

  <section class="card card-back" aria-label="Business card back">
    <div class="back-brand">
      <span class="brand-name">ElderNova</span>
      <span class="brand-suffix">LLC</span>
    </div>

    <div class="holder">
      <p class="holder-name">Mark Holloway</p>
      <p class="holder-title">President</p>
    </div>

    <div class="divider"></div>

    <ul class="contacts">
      <li>
        <svg viewBox="0 0 24 24" aria-hidden="true"><path d="M6.6 10.8a15.1 15.1 0 0 0 6.6 6.6l2.2-2.2a1 1 0 0 1 1-.25 11.4 11.4 0 0 0 3.6.6 1 1 0 0 1 1 1V20a1 1 0 0 1-1 1A17 17 0 0 1 3 4a1 1 0 0 1 1-1h3.5a1 1 0 0 1 1 1c0 1.25.2 2.45.6 3.6a1 1 0 0 1-.25 1z"/></svg>
        (555) 210-4477
      </li>
      <li>
        <svg viewBox="0 0 24 24" aria-hidden="true"><path d="M7 2h10a2 2 0 0 1 2 2v16a2 2 0 0 1-2 2H7a2 2 0 0 1-2-2V4a2 2 0 0 1 2-2zm0 3v13h10V5zm5 14.2a1 1 0 1 0 0 .01z"/></svg>
        (555) 318-2290
      </li>
      <li>
        <svg viewBox="0 0 24 24" aria-hidden="true"><path d="M2 5h20v14H2zm2 2v.5l8 5 8-5V7zm0 2.8V17h16V9.8l-8 5z"/></svg>
        Mark@ElderNova.com
      </li>
      <li>
        <svg viewBox="0 0 24 24" aria-hidden="true"><path d="M12 2a10 10 0 1 0 0 20 10 10 0 0 0 0-20zm6.9 6h-3a15 15 0 0 0-1.3-3.9A8 8 0 0 1 18.9 8zM12 4c.8 1.2 1.5 2.5 1.9 4h-3.8c.4-1.5 1.1-2.8 1.9-4zM4.3 14a8 8 0 0 1 0-4h3.4a16 16 0 0 0 0 4zm.8 2h3a15 15 0 0 0 1.3 3.9A8 8 0 0 1 5.1 16zm3-8h-3a8 8 0 0 1 4.3-3.9A15 15 0 0 0 8.1 8zM12 20c-.8-1.2-1.5-2.5-1.9-4h3.8c-.4 1.5-1.1 2.8-1.9 4zm2.3-6H9.7a14 14 0 0 1 0-4h4.6a14 14 0 0 1 0 4zm.3 5.9a15 15 0 0 0 1.3-3.9h3a8 8 0 0 1-4.3 3.9zm1.7-5.9a16 16 0 0 0 0-4h3.4a8 8 0 0 1 0 4z"/></svg>
        www.ElderNova.com
      </li>
    </ul>
  </section>

</body>
</html>
```